DWR Logistics Marketing flyer

Good morning, I run a trucking company and I will be needing help setting up a website logo and a marketing flyer or something like that talking about our services and what we can offer to potential new customers who need to ship their product. I need help getting this all together.

Target Market(s)

Transportation customers

Requirements
Must have
• should list our services and contact info
Nice to have
• the Logo on the top

```html
<!DOCTYPE html>
<html lang="en">
<head>
<meta charset="utf-8">
<title>DWR Logistics – Transport Solutions Flyer</title>
<link href="https://fonts.googleapis.com/css2?family=Montserrat:wght@400;600;800;900&family=Open+Sans:wght@400;600&display=swap" rel="stylesheet">
<style>
  :root{
    --navy:#14275a;
    --blue:#1f4fa0;
    --orange:#f26a2a;
    --text:#2b2f3a;
    --muted:#6b7280;
    --sky-top:#cfe3f6;
    --sky-bottom:#7aa4d6;
    --soft:#eef1f6;
  }
  *{box-sizing:border-box;margin:0;padding:0}
  html,body{width:849px;height:1200px;overflow:hidden;background:#fff}
  .flyer{position:relative;width:849px;height:1200px;overflow:hidden;background:#fff;font-family:"Open Sans",Arial,sans-serif;color:var(--text)}
  .brand{position:absolute;left:22px;top:30px;width:165px;display:flex;flex-direction:column;align-items:center;gap:10px}
  .brand-dot{width:56px;height:56px;border-radius:50%;background:var(--navy)}
  .brand-name{font-family:"Montserrat",sans-serif;font-weight:800;font-size:20px;line-height:1;color:var(--navy);white-space:nowrap}
  .headline{position:absolute;left:212px;top:18px;width:620px;font-family:"Montserrat",sans-serif;font-weight:900;font-size:37px;line-height:1.1;color:var(--orange);text-transform:uppercase}
  .headline .accent{color:var(--navy)}
  .hero{position:absolute;left:330px;top:150px;width:519px;height:290px;background:linear-gradient(180deg,var(--sky-top),var(--sky-bottom) 70%,#4d5a6b)}
  .hero-fade{position:absolute;left:330px;top:150px;width:140px;height:290px;background:linear-gradient(90deg,#fff,rgba(255,255,255,0))}
  .section{position:absolute}
  .section h2{font-family:"Montserrat",sans-serif;font-weight:800;font-size:18px;line-height:1.15;color:var(--navy);display:flex;gap:8px}
  .section h2::before{content:"";flex:0 0 11px;height:11px;border-radius:50%;background:var(--blue);margin-top:5px}
  .section.award h2::before{background:var(--orange)}
  .section p{margin-top:9px;font-size:10.6px;line-height:1.5}
  .s-efficient{left:22px;top:152px;width:305px}
  .s-coast{left:22px;top:450px;width:390px}
  .s-fast{left:22px;top:655px;width:390px}
  .award{left:440px;top:470px;width:390px}
  .badges{position:absolute;left:470px;top:810px;display:flex;gap:40px;align-items:center}
  .badge-circle{width:96px;height:96px;border-radius:50%;background:var(--navy)}
  .badge-rect{width:170px;height:80px;border-radius:6px;background:var(--soft);border:2px solid var(--blue)}
  .refs{position:absolute;left:22px;top:960px;width:390px;height:140px;border:1px solid #d8dce4;border-radius:8px;padding:14px 18px}
  .refs h3{font-family:"Montserrat",sans-serif;font-weight:800;font-size:14px;color:var(--navy);text-align:center}
  .ref-list{display:flex;justify-content:space-between;align-items:center;margin-top:22px}
  .ref-name{font-family:"Montserrat",sans-serif;font-weight:800;font-size:17px;color:var(--blue)}
  .ref-note{margin-top:16px;font-size:12px;text-align:center;color:var(--muted)}
  .contact{position:absolute;left:450px;top:975px;width:380px;display:flex;gap:14px}
  .pin{flex:0 0 34px}
  .contact h3{font-family:"Montserrat",sans-serif;font-weight:800;font-size:16px;color:var(--navy);margin-bottom:6px}
  .contact p{font-size:11.5px;line-height:1.6}
  .footer-band{position:absolute;left:0;bottom:0;width:849px;height:70px}
</style>
</head>
<body>
<div class="flyer">
  <div class="brand"><span class="brand-dot"></span><span class="brand-name">DWR Logistics</span></div>

  <h1 class="headline">Your trusted partner <span class="accent">for seamless</span> transport solutions!"</h1>

  <div class="hero" role="img" aria-label="Photo of a blue semi truck with a white trailer on the highway under a blue sky"></div>
  <div class="hero-fade"></div>

  <section class="section s-efficient">
    <h2>Efficient solutions, we lead the way in timely deliveries!"</h2>
    <p>DWR Logistics LLC is a transportation company that specializes in maximizing the efficiency in moving products from shipper to customer in the shortest, safest time possible. We have the knowledge and ability to haul on dry van, reefer, flatbed or tanker loads that need to be moved. We strive to be your number one call to bring or move any product that your company may need. With our current 30 truck fleet, we can service customers locally or across country with ease and we're ready to make sure that your product is to your customers in the time frame promised.</p>
  </section>

  <section class="section s-coast">
    <h2>From coast to coast, we delivers its products with pride and precision!"</h2>
    <p>We take pride in our work and our customer service from pick up to delivery. Our current customer list handles more than half of the nation's imported orange juice, hauling the corn oil that fries the potatoes chips for one of the nation's largest potato chip suppliers, to hauling wine from the west coast doing plant to plant transfers to the plants on the east coast. We also branch out to haul the corn syrup in to make the wine and alcohol out of the plant in the Midwest to the different plants that make alcohol. In short, from a transportation standpoint if you need it, we can bring it to you.</p>
  </section>

  <section class="section s-fast">
    <h2>Fast attention, quick results, immediate delivery</h2>
    <p>What sets us apart from any other carrier is that when you call you will get either the owner or the CFO, you will not have to wait for approvals and time wasted. We work through the problems to find the right solution then get it executed quickly and effectively. You are not just another number to us, you are what makes our company possible, and we value that relationship.</p>
  </section>

  <section class="section award">
    <h2>Award-winning excellence: We set the standard in transportation!"</h2>
    <p>To date, we have won the Summit Freight Link Elite Carrier Excellence Award two years in a row servicing their major customers across their different brokerage offices. We're the number one truck supplier to two of the major orange juice manufacturers in the US for when they bring their product into port side in Florida, and it needs to go to their manufacturing facility throughout the state. In the past year, we have hauled over 40 million gallons of orange juice, another million gallons of wine and alcohol and millions of gallons of corn oil to service the nation's food industry with the ability to add to that ever-growing number.</p>
  </section>

  <div class="badges">
    <div class="badge-circle" role="img" aria-label="Thirty years anniversary badge"></div>
    <div class="badge-rect" role="img" aria-label="Elite carrier award badge"></div>
  </div>

  <div class="refs">
    <h3>Our references include those from</h3>
    <div class="ref-list">
      <span class="ref-name">Norvale</span>
      <span class="ref-name">Citrafresh</span>
      <span class="ref-name">Crispo</span>
    </div>
    <p class="ref-note">and Brookfield Spirits</p>
  </div>

  <div class="contact">
    <svg class="pin" viewBox="0 0 24 32" width="34" height="45" aria-hidden="true">
      <path d="M12 0C5.4 0 0 5.3 0 11.9 0 20.8 12 32 12 32s12-11.2 12-20.1C24 5.3 18.6 0 12 0z" fill="var(--orange)"/>
      <circle cx="12" cy="12" r="4.5" fill="#fff"/>
    </svg>
    <div>
      <h3>Address &amp; Contact Information:</h3>
      <p>410 Maple Ct. Riverton, IN 47001<br>
      CEO: Evan Harlow | Phone: 555-201-4418<br>
      CFO: Nolan Pryce | Phone: 555-376-0925<br>
      hello@dwrlogistics.example</p>
    </div>
  </div>

  <svg class="footer-band" viewBox="0 0 849 70" preserveAspectRatio="none" aria-hidden="true">
    <path d="M0 40 C200 10 420 60 849 22 L849 70 L0 70 Z" fill="var(--soft)"/>
    <path d="M0 58 C260 38 520 72 849 50 L849 70 L0 70 Z" fill="var(--navy)"/>
  </svg>
</div>
</body>
</html>
```